Chimney Service company needs new business card design

We need a updated business card with our new logo added. We provide a full range of chimney services throughout Vermont and New Hampshire. The business card will be one sided and color. Attached is our current business card another document showing all the information we would like on the card.
We dont like a lot of flashy colors.... here is a link to our website to get an idea of our branding www.flueguardianvt.example

Target Market(s)

homeowners

Industry/Entity Type

Business

Contact Information for Business Card

See attached sheet for content.

Font styles to use
Serif
Sans Serif

Requirements
Must have
• all information provided on separate sheet
Should not have
• Additional information that may clogg up design

```html
<!DOCTYPE html>
<html lang="en">
<head>
<meta charset="utf-8">
<title>Flue Guardian Business Card</title>
<link href="https://fonts.googleapis.com/css2?family=PT+Sans:wght@400;700&family=Arimo:wght@700&display=swap" rel="stylesheet">
<style>
  :root {
    --crimson: #d4163f;
    --ink: #2a2a2a;
    --charcoal: #1e1e1e;
    --band-grey: #c9c9cb;
    --panel-grey: #e2e2e4;
    --backdrop: #e8ebed;
    --card: #ffffff;
  }
  * { margin: 0; padding: 0; box-sizing: border-box; }
  html, body { width: 1200px; height: 900px; overflow: hidden; background: var(--backdrop); }
  .card {
    position: absolute; left: 100px; top: 164px; width: 1000px; height: 572px;
    background: var(--card); overflow: hidden;
    box-shadow: 0 10px 30px rgba(0,0,0,0.12);
  }
  .decor-panel {
    position: absolute; right: 0; top: 150px; width: 280px; height: 385px;
    background: var(--panel-grey);
  }
  .decor-art {
    position: absolute; right: 40px; top: 175px; width: 200px; height: 300px;
    background: radial-gradient(ellipse at 45% 35%, rgba(212,22,63,0.2), rgba(212,22,63,0.06) 60%, rgba(200,200,202,0.35) 100%);
  }
  .brand {
    position: absolute; left: 70px; top: 80px; display: flex; align-items: center; gap: 18px;
  }
  .brand-square { width: 40px; height: 40px; background: var(--ink); }
  .brand-name {
    font-family: 'PT Sans', sans-serif; font-weight: 700; font-size: 38px;
    color: var(--ink); line-height: 1;
  }
  .services {
    position: absolute; left: 78px; top: 196px; list-style: none;
    font-family: 'PT Sans', sans-serif; font-size: 26px; line-height: 36px; color: var(--crimson);
  }
  .services li::before, .contact-list li::before {
    content: ""; display: inline-block; width: 7px; height: 7px; border-radius: 50%;
    background: var(--ink); margin-right: 16px; vertical-align: middle;
  }
  .service-area {
    position: absolute; right: 60px; top: 62px; text-align: right;
    font-family: 'Arimo', sans-serif; font-weight: 700; font-size: 26px; line-height: 36px; color: var(--ink);
  }
  .contact { position: absolute; left: 540px; top: 300px; font-family: 'PT Sans', sans-serif; }
  .contact-label { font-size: 26px; color: var(--ink); margin-bottom: 4px; }
  .contact-list { list-style: none; font-size: 26px; line-height: 36px; color: var(--crimson); }
  .bands { position: absolute; left: 0; right: 0; bottom: 0; }
  .band-grey { height: 12px; background: var(--band-grey); }
  .band-black { height: 9px; background: var(--charcoal); }
  .band-crimson { height: 16px; background: var(--crimson); }
</style>
</head>
<body>
  <div class="card">
    <div class="decor-panel"></div>
    <div class="decor-art" role="img" aria-label="Faint flame and brick chimney decoration"></div>

    <div class="brand">
      <div class="brand-square"></div>
      <div class="brand-name">Flue Guardian</div>
    </div>

    <ul class="services">
      <li>Full Masonry Services</li>
      <li>Historic Chimney Restoration</li>
      <li>Stainless Steel Liners</li>
      <li>New Chimney Installations</li>
      <li>CSIA Certified Chimney Sweeps</li>
      <li>Fully Insured – Free Estimates</li>
      <li>Family Owned And Aperated</li>
    </ul>

    <div class="service-area">
      <p>Serving VT &amp; NewHampshire</p>
      <p>Since 1989</p>
      <p>802-555-0147</p>
    </div>

    <div class="contact">
      <p class="contact-label">Contact:</p>
      <ul class="contact-list">
        <li>info@flueguardianvt.example</li>
        <li>www.flueguardianvt.example</li>
      </ul>
    </div>

    <div class="bands">
      <div class="band-grey"></div>
      <div class="band-black"></div>
      <div class="band-crimson"></div>
    </div>
  </div>
</body>
</html>
```